"Recently Leased" flyer for real estate agency

Looking to have a Recently Leased flyer designed. This will be delivered to apartments and houses closely situated to a property we have recently leased. The idea is to get the attention of owner/landlords in the area that may be considering leasing their property in the future and inform them of the great work we are doing locally. I would like the design to be a two sided flyer using the photoshop (PSD) template below (we would like to be able to edit this once complete should we need to update copy etc in the future). I would like the front page to look like our "for lease sign with the leased sticker on it and copy, I dont want it to look like a typical junk mail flyer.

Target Market(s)

Property owners and investors, male and female aged 28-70

Industry/Entity Type

Real Estate

Font styles to use
Sans Serif

Colors

Designer to choose colors to be used in the design.

Requirements
Must have
• Harbor Keystone Logo
• Contact information
• Copy supplied
Nice to have
• Slick, clean design,
Should not have
• too many colours or too busy a design.
• NO PROPERTY PHOTOS ON FRONT - I want this to be generic and not relate to a specific property image which might confuse people.

```html
<!DOCTYPE html>
<html lang="en">
<head>
<meta charset="utf-8">
<title>Harbor Keystone – Recently Leased Flyer</title>
<link rel="stylesheet" href="https://fonts.googleapis.com/css2?family=Source+Sans+3:wght@400;600;700&display=swap">
<style>
  :root {
    --page-bg: #e7e8ea;
    --teal: #1a8b98;
    --teal-deep: #0f7784;
    --photo-dark: #1f2b31;
    --photo-mid: #34464d;
    --ink: #1c1c1c;
    --tag: #161616;
    --white: #ffffff;
  }
  * { box-sizing: border-box; margin: 0; padding: 0; }
  html, body { width: 1200px; height: 1200px; overflow: hidden; }
  body {
    background: var(--page-bg);
    font-family: "Source Sans 3", "Myriad Pro", Arial, sans-serif;
    position: relative;
  }
  .flyer {
    position: absolute;
    top: 88px;
    width: 470px;
    height: 1024px;
    background: var(--white);
    overflow: hidden;
    box-shadow: 0 3px 10px rgba(0,0,0,.25);
  }
  .flyer--front { left: 122px; }
  .flyer--back { left: 608px; }
  .flyer__shapes { position: absolute; inset: 0; }
  .brand {
    position: absolute;
    left: 0; right: 0; top: 108px;
    display: flex; justify-content: center; align-items: center; gap: 10px;
    color: var(--white);
    font-weight: 600;
    font-size: 38px;
    letter-spacing: .5px;
    line-height: 1;
  }
  .brand__square { width: 14px; height: 14px; background: var(--white); }
  .intro {
    position: absolute; left: 20px; right: 20px;
    color: var(--white);
    text-align: center;
    font-size: 16px;
    line-height: 20.5px;
  }
  .flyer--front .intro { top: 238px; }
  .flyer--back .intro { top: 282px; }
  .benefits {
    position: absolute; left: 28px; right: 24px; top: 448px;
    list-style: none;
    color: var(--ink);
    font-size: 16.5px;
    line-height: 20.5px;
  }
  .benefits li { position: relative; padding-left: 36px; margin-bottom: 10.5px; }
  .benefits li::before {
    content: ""; position: absolute; left: 6px; top: 5px;
    width: 12px; height: 12px; border-radius: 50%;
    background: var(--teal);
  }
  .services {
    position: absolute; left: 36px; right: 24px; top: 395px;
    list-style: none;
    color: var(--ink);
    font-size: 16.5px;
    line-height: 20.5px;
  }
  .services li { position: relative; padding-left: 18px; margin-bottom: 10.5px; }
  .services li::before {
    content: ""; position: absolute; left: 0; top: 7px;
    width: 7px; height: 7px; border-radius: 50%; background: var(--ink);
  }
  .call-to-action {
    position: absolute; left: 14px; right: 14px;
    color: var(--teal-deep);
    text-align: center;
    font-size: 16.5px;
    line-height: 20.5px;
  }
  .flyer--front .call-to-action { top: 759px; }
  .flyer--back .call-to-action { top: 759px; }
  .agent-tag {
    position: absolute; left: 115px; top: 860px;
    width: 245px; height: 68px;
    color: var(--white);
    text-align: center;
  }
  .agent-tag svg { position: absolute; inset: 0; }
  .agent-tag__name {
    position: relative; display: block;
    font-weight: 600; font-size: 35px; line-height: 1; padding-top: 12px;
  }
  .agent-tag__agency {
    position: relative; display: block;
    font-size: 12.5px; font-weight: 600; letter-spacing: .3px; margin-top: 1px;
  }
  .contact {
    position: absolute; left: 0; right: 0; top: 935px;
    color: var(--white);
    text-align: center;
    font-weight: 600;
    font-size: 16.5px;
    line-height: 20.5px;
  }
</style>
</head>
<body>

<section class="flyer flyer--front" aria-label="Flyer front">
  <svg class="flyer__shapes" width="470" height="1024" viewBox="0 0 470 1024">
    <defs>
      <linearGradient id="photo-front" x1="0" y1="0" x2="0" y2="1">
        <stop offset="0" stop-color="#1c2a32"/>
        <stop offset=".55" stop-color="#35474d"/>
        <stop offset="1" stop-color="#26332f"/>
      </linearGradient>
    </defs>
    <polygon points="0,0 470,0 470,436 0,418" fill="var(--teal)"/>
    <polygon points="0,0 470,0 470,428 0,408" fill="url(#photo-front)" role="img" aria-label="Darkened photo of a modern townhouse street"/>
    <polygon points="0,880 470,900 470,1024 0,1024" fill="var(--teal-deep)"/>
  </svg>

  <div class="brand"><span class="brand__square"></span>HARBOR KEYSTONE</div>

  <p class="intro">We recently leased a property in your building or street. Attracting a great reliable tenant and fantastic return for the owner.<br>We received a high number of enquires and applications for this property and have a database of screened and qualified tenants looking to lease in your area.</p>

  <ul class="benefits">
    <li>On average we lease properties 2 weeks faster than the Northern Beaches average</li>
    <li>Strong database of tenants actively looking in the area</li>
    <li>All we do is lease property, no sales – so tenanting and managing your property is our priority</li>
    <li>90 day money back guarantee on our level of service</li>
    <li>Highly competitive, simple all-inclusive pricing.</li>
    <li>Experience the difference of a property management specialist</li>
  </ul>

  <p class="call-to-action">Contact Sam to get your free rental appraisal or transfer your existing investment to an agency that will give it the attention it deserves and maxamise your return.</p>

  <div class="agent-tag">
    <svg width="245" height="68" viewBox="0 0 245 68"><polygon points="0,0 245,9 245,68 0,68" fill="var(--tag)"/></svg>
    <span class="agent-tag__name">SAM CARVER</span>
    <span class="agent-tag__agency">HARBOR KEYSTONE AGENCY</span>
  </div>

  <p class="contact">Level 2, 18 Marlow St, Eastvale NSW 2100<br>www.harborkeystone.com.au<br>0400 555 218 | sam@harborkeystone.com.au</p>
</section>

<section class="flyer flyer--back" aria-label="Flyer back">
  <svg class="flyer__shapes" width="470" height="1024" viewBox="0 0 470 1024">
    <defs>
      <linearGradient id="photo-back" x1="0" y1="0" x2="1" y2="1">
        <stop offset="0" stop-color="#1d2224"/>
        <stop offset=".6" stop-color="#3a3430"/>
        <stop offset="1" stop-color="#4a3a30"/>
      </linearGradient>
    </defs>
    <polygon points="0,0 470,0 470,388 0,370" fill="var(--teal)"/>
    <polygon points="0,0 470,0 470,380 0,360" fill="url(#photo-back)" role="img" aria-label="Darkened photo of a brick home with a covered patio"/>
    <polygon points="0,880 470,900 470,1024 0,1024" fill="var(--teal-deep)"/>
  </svg>

  <div class="brand"><span class="brand__square"></span>HARBOR KEYSTONE</div>

  <p class="intro">The fundamental idea behind Harbor Keystone Agency was to give landlords a simple and confidence inspiring experience. We achieve this through:</p>

  <ul class="services">
    <li>Unique marketing that goes beyond the standard listing sites and has seen our average days-on-market at 5.9days for 2018.</li>
    <li>A simple, yet competitive fee structure.</li>
    <li>Excellent customer service through an experienced professional property manager.</li>
    <li>Sound advice and communication through out the leasing and management process.</li>
    <li>A simple yet powerful landlord portal which enables owners to view media rich inspection reports, financial reports and maintenance progress at anytime.</li>
    <li>We then back our service promise with a 90day money back guarantee.</li>
  </ul>

  <p class="call-to-action">If you have been considering leasing your property, purchasing a local investment or aren’t happy with your current managing agency, please don’t hesitate to contact your local rental specialist for more information:</p>

  <div class="agent-tag">
    <svg width="245" height="68" viewBox="0 0 245 68"><polygon points="0,0 245,9 245,68 0,68" fill="var(--tag)"/></svg>
    <span class="agent-tag__name">SAM CARVER</span>
    <span class="agent-tag__agency">HARBOR KEYSTONE AGENCY</span>
  </div>

  <p class="contact">Level 2, 18 Marlow St, Eastvale NSW 2100<br>www.harborkeystone.com.au<br>0400 555 218 | sam@harborkeystone.com.au</p>
</section>

</body>
</html>
```